Stationery Design Project

We need letterhead and business cards designed for our consulting firm. Color scheme, mostly deep blue (see logo). We are a commercial consulting work out firm, nationwide (large loans, $10MM and up). Visit our website for more info.
Updates

Project Deadline Extended
Reason: Meeting tomorrow morning to make final final decision. Would like this project to stay open to be able to provide feed back and receive final edits and approve. Thank you!!!

Target Market(s)

High end investors

Industry/Entity Type

Business

Requirements
Must have
• Letterhead must have the logo and the address

4817 Larkmoor Avenue, Suite 210, San Diego, CA 92107
Nice to have
• It would be nice to incorporate a watermark of all or some portion of the logo on the letterhead, or at least for the 2nd sheets.

Maybe our phone number: 858.555.0174
and/or webiste: www.tollandridgecap.example
Should not have
• Target users and audience of this will be men so, frilly or whimsical type designs are not preferred.

```html
<!DOCTYPE html>
<html lang="en">
<head>
<meta charset="utf-8">
<title>Tolland Ridge Capital – Letterhead</title>
<link href="https://fonts.googleapis.com/css2?family=Open+Sans:wght@400;600;700&display=swap" rel="stylesheet">
<style>
  :root {
    --brand-blue: #1f4f86;
    --rule-grey: #8a8d91;
    --text-grey: #55585c;
    --watermark: #ececec;
    --paper: #ffffff;
  }
  * { margin: 0; padding: 0; box-sizing: border-box; }
  html, body { width: 867px; height: 1200px; overflow: hidden; background: var(--paper); }
  body { font-family: "Open Sans", Arial, sans-serif; }
  .letterhead { position: relative; width: 867px; height: 1200px; }

  .brand {
    position: absolute; left: 48px; top: 72px;
    display: flex; align-items: center; gap: 12px;
  }
  .brand-mark { width: 22px; height: 22px; background: var(--brand-blue); }
  .brand-name {
    font-weight: 600; font-size: 34px; letter-spacing: 1px;
    color: var(--brand-blue); text-transform: uppercase; line-height: 1;
  }

  .header-rule {
    position: absolute; left: 48px; right: 48px; top: 152px;
    height: 3px; background: var(--rule-grey);
  }

  .contact {
    position: absolute; right: 60px; top: 68px;
    text-align: right; color: var(--brand-blue);
    font-size: 14px; font-weight: 700; line-height: 19px;
  }

  .watermark {
    position: absolute; left: 0; right: 0; top: 520px;
    text-align: center; color: var(--watermark);
    font-weight: 700; font-size: 64px; letter-spacing: 4px;
    text-transform: uppercase;
  }

  .footer-rule {
    position: absolute; left: 36px; right: 36px; top: 1106px;
    height: 3px; background: var(--rule-grey);
  }
  .footer-name {
    position: absolute; left: 50%; top: 1088px; transform: translateX(-50%);
    background: var(--paper); padding: 0 14px;
    color: var(--brand-blue); font-weight: 600; font-size: 16px;
    letter-spacing: 1px; text-transform: uppercase; white-space: nowrap;
  }
  .footer-web {
    position: absolute; left: 0; right: 0; top: 1126px;
    text-align: center; color: var(--text-grey); font-size: 12px;
  }
</style>
</head>
<body>
  <main class="letterhead">
    <header>
      <div class="brand">
        <span class="brand-mark"></span>
        <span class="brand-name">Tolland Ridge Capital</span>
      </div>
      <address class="contact">
        4817 Larkmoor Avenue, Suite 210<br>
        San Diego, CA 92107<br>
        Tel:858.555.0174
      </address>
      <div class="header-rule"></div>
    </header>

    <div class="watermark" aria-hidden="true">Tolland Ridge</div>

    <footer>
      <div class="footer-rule"></div>
      <div class="footer-name">Tolland Ridge Capital</div>
      <div class="footer-web">http://www.tollandridgecap.example</div>
    </footer>
  </main>
</body>
</html>
```